Most captivating card ever!

Life Coach - Professional Adventurer - Entrepreneur
I need the worlds most amazing business card for my personal brand. This business card will mostly be used to give to prospective clients for life coaching and business coaching.
Be creative, be adventurous. It needs to stand out. Make people say.. I need this guy!
My background is as an entrepreneur and professional adventurer undertaking extreme expeditions. I am now moving into life coaching.
No specific design ideas, so you have full creativity. Show me your best.
Industry/Entity Type
Life Coaching
Contact Information for Business Card
Dan Pellow
itsdanp.com.au
0468215903
Colors
Designer to choose colors to be used in the design.
Look and feel

```html
<!DOCTYPE html>
<html lang="en">
<head>
<meta charset="utf-8">
<title>Dan Pellow — Business Card</title>
<link rel="stylesheet" href="https://fonts.googleapis.com/css2?family=Bebas+Neue&display=swap">
<style>
  :root {
    --page-bg: #e6dfde;
    --card-black: #0f0606;
    --card-deep: #3a0808;
    --brand-red: #d8161a;
    --map-red: #e01b1f;
    --name-dark: #3c0a0a;
    --text-white: #ffffff;
  }
  * { margin: 0; padding: 0; box-sizing: border-box; }
  html, body {
    width: 1200px;
    height: 800px;
    overflow: hidden;
    background: var(--page-bg);
  }
  .canvas {
    position: relative;
    width: 1200px;
    height: 800px;
  }
  .business-card {
    position: absolute;
    left: 100px;
    top: 119px;
    width: 1000px;
    height: 562px;
    background: var(--card-black);
    overflow: hidden;
    font-family: "Bebas Neue", sans-serif;
    box-shadow: 0 6px 20px rgba(0,0,0,0.18);
  }
  .world-network {
    position: absolute;
    left: 0;
    top: 0;
    width: 100%;
    height: 322px;
    background:
      radial-gradient(ellipse 32% 45% at 62% 20%, rgba(224,27,31,0.55), transparent 70%),
      radial-gradient(ellipse 55% 70% at 55% 10%, rgba(120,12,14,0.8), transparent 75%),
      linear-gradient(180deg, var(--card-deep) 0%, var(--card-black) 85%);
  }
  .tagline {
    position: absolute;
    left: 61px;
    top: 258px;
    color: var(--text-white);
    font-size: 36px;
    letter-spacing: 1.6px;
    white-space: nowrap;
  }
  .tagline .divider {
    color: var(--brand-red);
    margin: 0 8px;
  }
  .name-band {
    position: absolute;
    left: 0;
    top: 322px;
    width: 100%;
    height: 240px;
    background: var(--brand-red);
  }
  .holder-name {
    position: absolute;
    left: 61px;
    top: 4px;
    font-size: 128px;
    line-height: 0.8;
    letter-spacing: 1px;
  }
  .holder-name .first { display: block; color: var(--name-dark); }
  .holder-name .last { display: block; color: var(--text-white); margin-top: 10px; }
  .contact-list {
    position: absolute;
    left: 605px;
    top: 62px;
    list-style: none;
    color: var(--text-white);
    font-size: 46px;
    line-height: 57px;
    letter-spacing: 1.5px;
  }
</style>
</head>
<body>
  <main class="canvas">
    <article class="business-card">
      <div class="world-network" role="img" aria-label="World map with connected network lines, highlighting Australia"></div>
      <p class="tagline">Life Coach<span class="divider">|</span>Professional Adventurer<span class="divider">|</span>Entrepreneur</p>
      <section class="name-band">
        <h1 class="holder-name">
          <span class="first">Dan</span>
          <span class="last">Pellow</span>
        </h1>
        <ul class="contact-list">
          <li>M : 0468 215 903</li>
          <li>W : itsdanp.com.au</li>
        </ul>
      </section>
    </article>
  </main>
</body>
</html>
```